Visitenkarten-Design für Vermittlung und Verkauf von Immobilien
Perfekte Umsetzung meiner Wünsche, sowie auch selbständige Einbringung von Ideen. Sehr zu empfehlen!
Zielgruppe
Immobilien vermitteln, verkaufen

```html
<!DOCTYPE html>
<html lang="de">
<head>
<meta charset="utf-8">
<title>ORTAVEN Immobilien – Visitenkarte</title>
<link rel="stylesheet" href="https://fonts.googleapis.com/css2?family=Open+Sans:wght@400;600&display=swap">
<style>
  :root {
    --stage: #000000;
    --paper: #ffffff;
    --navy: #172a45;
    --ink: #111418;
    --muted: #5b5f66;
    --band-grey: #6b6c6f;
    --stripe: #3d4760;
    --accent-blue: #2aa3dc;
    --rule: #2c3a55;
  }
  * { box-sizing: border-box; margin: 0; padding: 0; }
  html, body {
    width: 1200px; height: 1200px; overflow: hidden;
    background: var(--stage);
    font-family: "Open Sans", Arial, sans-serif;
  }
  .canvas { position: relative; width: 1200px; height: 1200px; }

  .card {
    position: absolute; left: 284px; width: 610px; height: 395px;
    overflow: hidden;
  }
  .card--front { top: 91px; background: var(--paper); }
  .card--back { top: 564px; background: var(--navy); }

  /* front: upper area */
  .holder { position: absolute; left: 66px; top: 142px; }
  .holder__name { font-size: 23px; font-weight: 400; color: var(--ink); line-height: 1.2; }
  .holder__role { font-size: 18px; color: var(--muted); margin-top: 4px; }

  .brand {
    position: absolute; left: 355px; top: 120px; width: 220px;
    display: flex; flex-direction: column; align-items: center; gap: 14px;
  }
  .brand__mark { width: 46px; height: 46px; background: var(--navy); }
  .brand__name {
    font-size: 24px; font-weight: 600; letter-spacing: 4px; color: var(--navy);
    white-space: nowrap;
  }

  .divider {
    position: absolute; left: 0; right: 0; top: 241px; height: 2px; background: var(--rule);
  }

  /* front: contact area */
  .address {
    position: absolute; left: 64px; top: 272px;
    display: flex; gap: 8px; font-size: 15px; color: var(--muted); line-height: 1.45;
  }
  .address svg { width: 14px; height: 20px; margin-top: 2px; flex: none; }

  .contacts {
    position: absolute; left: 378px; top: 254px; list-style: none;
    font-size: 15px; color: var(--muted);
  }
  .contacts li { display: flex; align-items: center; gap: 9px; height: 27px; }
  .contacts svg { width: 18px; height: 18px; flex: none; }

  .footer-band { position: absolute; left: 0; bottom: 0; width: 610px; height: 42px; }
  .footer-band svg { position: absolute; inset: 0; }
  .web {
    position: absolute; right: 36px; bottom: 9px;
    display: flex; align-items: center; gap: 10px;
    color: var(--paper); font-size: 16px;
  }
  .web svg { width: 16px; height: 16px; }

  /* back */
  .back-brand {
    position: absolute; left: 0; right: 0; top: 120px;
    display: flex; flex-direction: column; align-items: center; gap: 40px;
  }
  .back-brand__mark { width: 90px; height: 90px; background: var(--paper); }
  .back-brand__name {
    font-size: 48px; font-weight: 600; letter-spacing: 12px; color: var(--paper);
    padding-left: 12px; white-space: nowrap;
  }
</style>
</head>
<body>
<main class="canvas">

  <section class="card card--front" aria-label="Vorderseite">
    <div class="holder">
      <p class="holder__name">Lena Sorvath</p>
      <p class="holder__role">Geschäftsführend</p>
    </div>

    <div class="brand">
      <span class="brand__mark" aria-hidden="true"></span>
      <span class="brand__name">ORTAVEN</span>
    </div>

    <div class="divider"></div>

    <div class="address">
      <svg viewBox="0 0 14 20" aria-hidden="true">
        <path d="M7 0C3.1 0 0 3.1 0 7c0 5 7 13 7 13s7-8 7-13c0-3.9-3.1-7-7-7z" fill="var(--accent-blue)"/>
        <circle cx="7" cy="7" r="2.8" fill="#fff"/>
      </svg>
      <p>Am Lindenhang 14<br>55130 Wendelsfeld</p>
    </div>

    <ul class="contacts">
      <li>
        <svg viewBox="0 0 18 18" aria-hidden="true">
          <path d="M4 1l3 4-2 2c1 2 3 4 5 5l2-2 4 3-2 3C8 16 2 10 1 4z" fill="var(--muted)"/>
        </svg>
        00000/ 4417720
      </li>
      <li>
        <svg viewBox="0 0 18 18" aria-hidden="true">
          <rect x="4" y="1" width="10" height="5" fill="var(--muted)"/>
          <rect x="1" y="6" width="16" height="7" rx="1" fill="var(--muted)"/>
          <rect x="4" y="11" width="10" height="6" fill="var(--accent-blue)"/>
        </svg>
        00000/ 4417735
      </li>
      <li>
        <svg viewBox="0 0 18 18" aria-hidden="true">
          <rect x="1" y="4" width="16" height="11" fill="var(--muted)"/>
          <path d="M1 4l8 6 8-6" fill="none" stroke="#fff" stroke-width="1.4"/>
        </svg>
        info@ortaven.online
      </li>
    </ul>

    <div class="footer-band" aria-hidden="true">
      <svg viewBox="0 0 610 42" width="610" height="42">
        <rect x="0" y="16" width="280" height="26" fill="var(--band-grey)"/>
        <polygon points="262,42 278,16 294,16 278,42" fill="var(--stripe)"/>
        <polygon points="290,42 306,16 322,16 306,42" fill="var(--stripe)"/>
        <polygon points="318,42 334,16 350,16 334,42" fill="var(--stripe)"/>
        <polygon points="346,42 362,16 378,16 362,42" fill="var(--stripe)"/>
        <polygon points="344,42 370,0 610,0 610,42" fill="var(--navy)"/>
      </svg>
    </div>
    <div class="web">
      <svg viewBox="0 0 16 16" aria-hidden="true">
        <circle cx="8" cy="8" r="7" fill="var(--accent-blue)"/>
        <path d="M1 8h14M8 1v14M3 4h10M3 12h10" stroke="#fff" stroke-width="0.9" fill="none"/>
        <ellipse cx="8" cy="8" rx="3" ry="7" stroke="#fff" stroke-width="0.9" fill="none"/>
      </svg>
      www.ortaven.online
    </div>
  </section>

  <section class="card card--back" aria-label="Rückseite">
    <div class="back-brand">
      <span class="back-brand__mark" aria-hidden="true"></span>
      <span class="back-brand__name">ORTAVEN</span>
    </div>
  </section>

</main>
</body>
</html>
```